Etiketten für Olivenöl-Intensivcreme
Zielgruppe
Wir produzieren Bio-Food, u.a. Wein und Olivenöl. Jetzt soll eine Olivenöl-Intensivcreme im Bereich Kosmetik auf dem Markt platziert werden. Unsere Zielgruppe hat ein sehr breites Altersspektrum (jung bis alt), ist naturverbunden, tierlieb, gebildet, kritisch-reflektierend, weiß gute Qualität zu schätzen, ist überwiegend weiblich. Die Olivenöl-Intensivcreme hat eine sehr breite Verwendung und soll sich als 'Allzweckwaffe' in jedem Haushalt etablieren (Babyhaut-Pflege, Lippenpflege, Ganzkörperpflege, Hand-Schutzcreme etc.).
Aufgabenstellung
Die Creme soll heißen: Veltara (es könnte z.B. der Buchstabe 'O' durch eine Olive ersetzt werden). Es gibt zwei Etikette (Deckeloberseite der Metalldose und auf dem Boden). Der Durchmesser der Etikette ist jeweils 5,5 cm. Die Deckelunterseite gilt reinen Pflichtangaben. Im Dateidownloadbereich sind die Textvorgaben für die Etikette. MUT zur Farbe! Wir sind NICHT brav und angepasst! Orange kann Akzente setzen bzw. für Aufmerksamkeit im Regal sorgen.

```html
<!DOCTYPE html>
<html lang="de">
<head>
<meta charset="utf-8">
<title>Veltara – Etikettenentwürfe</title>
<link href="https://fonts.googleapis.com/css2?family=Josefin+Sans:wght@300;400;700&family=Oswald:wght@500&display=swap" rel="stylesheet">
<style>
  :root {
    --backdrop: #d9d9d9;
    --label: #ffffff;
    --olive: #aba219;
    --forest: #143a30;
    --orange: #f39200;
    --orange-soft: #f8b756;
    --cream: #fdeedc;
    --wreath: #7d9a4d;
    --ink: #1d2a27;
  }
  html, body {
    margin: 0;
    width: 1200px;
    height: 1200px;
    overflow: hidden;
    background: var(--backdrop);
  }
  .sheet {
    position: relative;
    width: 1200px;
    height: 1200px;
  }
  .variant-letter {
    position: absolute;
    font-family: "Josefin Sans", sans-serif;
    font-weight: 300;
    font-size: 34px;
    color: #111;
  }
  .label {
    position: absolute;
    width: 510px;
    height: 510px;
  }
  .label-a { left: 70px;  top: 62px; }
  .label-b { left: 620px; top: 63px; }
  .label-c { left: 70px;  top: 618px; }
  .label-d { left: 620px; top: 618px; }
  .label svg { width: 100%; height: 100%; display: block; }

  .brand-name { font-family: "Josefin Sans", sans-serif; font-weight: 400; font-size: 35px; text-anchor: middle; }
  .brand-olive { fill: var(--olive); }
  .brand-orange { fill: var(--orange); }
  .product-name { font-family: "Josefin Sans", sans-serif; font-weight: 700; fill: var(--forest); }
  .product-dot { fill: var(--olive); }
  .caps { font-family: "Josefin Sans", sans-serif; font-weight: 300; font-variant: small-caps; text-anchor: middle; letter-spacing: 1px; }
  .caps-light { fill: #ffffff; }
  .caps-olive { fill: var(--olive); }
  .caps-dark  { fill: var(--ink); }
  .badge-disc { fill: var(--forest); }
  .badge-text { font-family: "Oswald", sans-serif; font-weight: 500; fill: #ffffff; text-anchor: middle; }
</style>
</head>
<body>
<main class="sheet">
  <span class="variant-letter" style="left:68px;top:58px;">A</span>
  <span class="variant-letter" style="left:1107px;top:58px;">B</span>
  <span class="variant-letter" style="left:68px;top:1096px;">C</span>
  <span class="variant-letter" style="left:1110px;top:1096px;">D</span>

  <!-- Variant A: olive wreath -->
  <div class="label label-a">
    <svg viewBox="0 0 820 820">
      <circle cx="410" cy="410" r="410" fill="var(--label)"/>
      <circle cx="410" cy="410" r="340" fill="none" stroke="var(--wreath)" stroke-width="80" opacity="0.55" role="img" aria-label="Kranz aus Olivenzweigen mit Blättern und Oliven"/>
      <circle cx="410" cy="410" r="316" fill="var(--label)" stroke="var(--forest)" stroke-width="13"/>
      <circle cx="410" cy="410" r="297" fill="none" stroke="var(--olive)" stroke-width="4"/>
      <text class="brand-name brand-olive" x="418" y="252">KORVAL.HOF</text>
      <ellipse class="product-dot" cx="222" cy="315" rx="50" ry="62"/>
      <text class="product-name" x="285" y="370" font-size="122" textLength="360" lengthAdjust="spacingAndGlyphs">Veltara</text>
      <rect x="236" y="400" width="348" height="172" fill="none" stroke="var(--olive)" stroke-width="4"/>
      <rect x="246" y="412" width="328" height="98" fill="var(--olive)"/>
      <text class="caps caps-light" x="410" y="456" font-size="42">Olivenöl</text>
      <text class="caps caps-light" x="410" y="494" font-size="42">Intensivcreme</text>
      <text class="caps caps-olive" x="410" y="552" font-size="42">Naturkosmetik</text>
      <text class="caps caps-dark" x="405" y="622" font-size="42">Pflege- und</text>
      <text class="caps caps-dark" x="410" y="660" font-size="42">Schutzcreme</text>
      <circle class="badge-disc" cx="638" cy="642" r="66"/>
      <text class="badge-text" x="638" y="650" font-size="27">Bio-Olive</text>
      <text class="badge-text" x="638" y="684" font-size="27">Vegan</text>
    </svg>
  </div>

  <!-- Variant B: large sun rays -->
  <div class="label label-b">
    <svg viewBox="0 0 820 820">
      <circle cx="410" cy="410" r="410" fill="var(--label)"/>
      <circle cx="410" cy="410" r="365" fill="none" stroke="var(--orange-soft)" stroke-width="60" role="img" aria-label="Sonnenstrahlen rund um den Ring"/>
      <circle cx="410" cy="410" r="320" fill="var(--label)" stroke="var(--orange)" stroke-width="30"/>
      <circle cx="410" cy="410" r="298" fill="none" stroke="var(--olive)" stroke-width="4"/>
      <text class="brand-name brand-olive" x="418" y="252">KORVAL.HOF</text>
      <ellipse class="product-dot" cx="222" cy="315" rx="50" ry="62"/>
      <text class="product-name" x="285" y="370" font-size="122" textLength="360" lengthAdjust="spacingAndGlyphs">Veltara</text>
      <rect x="236" y="400" width="348" height="172" fill="none" stroke="var(--olive)" stroke-width="4"/>
      <rect x="246" y="412" width="328" height="98" fill="var(--olive)"/>
      <text class="caps caps-light" x="410" y="456" font-size="42">Olivenöl</text>
      <text class="caps caps-light" x="410" y="494" font-size="42">Intensivcreme</text>
      <text class="caps caps-olive" x="410" y="552" font-size="42">Naturkosmetik</text>
      <text class="caps caps-dark" x="405" y="622" font-size="42">Pflege- und</text>
      <text class="caps caps-dark" x="410" y="660" font-size="42">Schutzcreme</text>
      <circle class="badge-disc" cx="638" cy="638" r="66"/>
      <text class="badge-text" x="638" y="646" font-size="27">Bio-Olive</text>
      <text class="badge-text" x="638" y="680" font-size="27">Vegan</text>
    </svg>
  </div>

  <!-- Variant C: small sun rays -->
  <div class="label label-c">
    <svg viewBox="0 0 820 820">
      <circle cx="410" cy="410" r="410" fill="var(--label)"/>
      <circle cx="410" cy="410" r="375" fill="none" stroke="var(--orange-soft)" stroke-width="32" role="img" aria-label="Kleine Sonnenstrahlen rund um den Ring"/>
      <circle cx="410" cy="410" r="335" fill="var(--label)" stroke="var(--orange)" stroke-width="30"/>
      <circle cx="410" cy="410" r="310" fill="none" stroke="var(--olive)" stroke-width="4"/>
      <text class="brand-name brand-orange" x="410" y="240">KORVAL.HOF</text>
      <ellipse class="product-dot" cx="222" cy="315" rx="50" ry="62"/>
      <text class="product-name" x="285" y="370" font-size="122" textLength="360" lengthAdjust="spacingAndGlyphs">Veltara</text>
      <rect x="236" y="400" width="348" height="172" fill="none" stroke="var(--olive)" stroke-width="4"/>
      <rect x="246" y="412" width="328" height="98" fill="var(--olive)"/>
      <text class="caps caps-light" x="410" y="456" font-size="42">Olivenöl</text>
      <text class="caps caps-light" x="410" y="494" font-size="42">Intensivcreme</text>
      <text class="caps caps-olive" x="410" y="552" font-size="42">Naturkosmetik</text>
      <text class="caps caps-dark" x="405" y="622" font-size="42">Pflege- und</text>
      <text class="caps caps-dark" x="410" y="660" font-size="42">Schutzcreme</text>
      <circle class="badge-disc" cx="638" cy="642" r="66"/>
      <text class="badge-text" x="638" y="650" font-size="27">Bio-Olive</text>
      <text class="badge-text" x="638" y="684" font-size="27">Vegan</text>
    </svg>
  </div>

  <!-- Variant D: sunburst background -->
  <div class="label label-d">
    <svg viewBox="0 0 820 820">
      <defs>
        <radialGradient id="sunburst-glow" cx="0.5" cy="0.35" r="0.65">
          <stop offset="0" stop-color="#ffffff"/>
          <stop offset="1" stop-color="var(--cream)"/>
        </radialGradient>
      </defs>
      <circle cx="410" cy="410" r="410" fill="var(--label)"/>
      <circle cx="410" cy="410" r="371" fill="none" stroke="var(--orange)" stroke-width="34"/>
      <circle cx="410" cy="410" r="342" fill="url(#sunburst-glow)" role="img" aria-label="Zarte Sonnenstrahlen im Hintergrund"/>
      <circle cx="410" cy="410" r="342" fill="none" stroke="var(--olive)" stroke-width="4"/>
      <text class="brand-name brand-orange" x="420" y="230" font-size="40">KORVAL.HOF</text>
      <ellipse class="product-dot" cx="192" cy="307" rx="58" ry="74"/>
      <text class="product-name" x="265" y="375" font-size="140" textLength="420" lengthAdjust="spacingAndGlyphs">Veltara</text>
      <rect x="218" y="403" width="386" height="176" fill="none" stroke="var(--olive)" stroke-width="4"/>
      <rect x="230" y="415" width="362" height="104" fill="var(--olive)"/>
      <text class="caps caps-light" x="411" y="462" font-size="46">Olivenöl</text>
      <text class="caps caps-light" x="411" y="506" font-size="46">Intensivcreme</text>
      <text class="caps caps-olive" x="411" y="566" font-size="46">Naturkosmetik</text>
      <text class="caps caps-dark" x="405" y="646" font-size="46">Pflege- und</text>
      <text class="caps caps-dark" x="410" y="690" font-size="46">Schutzcreme</text>
      <circle class="badge-disc" cx="647" cy="627" r="56"/>
      <text class="badge-text" x="647" y="633" font-size="23">Bio-Olive</text>
      <text class="badge-text" x="647" y="662" font-size="23">Vegan</text>
    </svg>
  </div>
</main>
</body>
</html>
```